Building sign design

We need a sign design for the front of our automotive workshop building. The sign needs to fit the colours of our building and company. (black, red, grey and white). The sign needs to stand out and be a modern.

Sign is to replace the red Pennock Cells sign. 2900mmx2900mm.
Company logo attached (Highgear).
Also photos of old sign and building.

Sign needs to feature Highgear logo at top and what we do below.

-Warrant of Fitness
-Vehicle Servicing
-All Mechanical Repairs
-Tyres & Wheel Alignments
-Batteries & Diagnostics
-Automotive Parts
-Vehicle Sales.

Also needs a large "WOF" somewhere on sign.

And contact details at bottom of sign.
48 Tamsin Road
07 542 3917

```html
<!DOCTYPE html>
<html lang="en">
<head>
<meta charset="utf-8">
<title>Highgear Total Automotive – Building Sign</title>
<link rel="stylesheet" href="https://fonts.googleapis.com/css2?family=Michroma&family=Outfit:wght@500;600&display=swap">
<style>
  :root {
    --black: #000000;
    --red: #e31e26;
    --white: #ffffff;
    --grey-light: #5d5d5f;
    --grey-mid: #4a4a4c;
    --grey-dark: #2c2c2c;
  }
  html, body {
    margin: 0;
    padding: 0;
    width: 1200px;
    height: 1200px;
    overflow: hidden;
    background: var(--black);
  }
  .sign {
    position: relative;
    width: 1200px;
    height: 1200px;
    overflow: hidden;
    background: var(--black);
    font-family: "Michroma", sans-serif;
    color: var(--white);
  }
  .sign-art {
    position: absolute;
    inset: 0;
  }
  .brand {
    position: absolute;
    left: 0;
    width: 1200px;
    top: 58px;
    text-align: center;
  }
  .brand-name {
    margin: 0;
    font-family: "Michroma", sans-serif;
    font-size: 82px;
    line-height: 1;
    letter-spacing: 8px;
    color: var(--red);
  }
  .brand-tagline {
    margin: 26px 0 0;
    font-family: "Michroma", sans-serif;
    font-size: 30px;
    line-height: 1;
    letter-spacing: 10px;
    color: var(--white);
  }
  .services {
    list-style: none;
    margin: 0;
    padding: 0;
  }
  .service {
    position: absolute;
    font-size: 29px;
    line-height: 1;
    letter-spacing: 3px;
    white-space: nowrap;
    color: var(--white);
    transform: translateY(-50%);
  }
  .contact {
    position: absolute;
    left: 0;
    width: 1200px;
    top: 1034px;
    text-align: center;
    font-family: "Outfit", sans-serif;
    color: var(--white);
  }
  .contact-address {
    margin: 0;
    font-size: 50px;
    font-weight: 500;
    line-height: 1;
  }
  .contact-phone {
    margin: 22px 0 0;
    font-size: 88px;
    font-weight: 600;
    line-height: 1;
    letter-spacing: 1px;
  }
</style>
</head>
<body>
<main class="sign">
  <svg class="sign-art" width="1200" height="1200" viewBox="0 0 1200 1200" aria-hidden="true">
    <defs>
      <linearGradient id="ring-fill" x1="0" y1="0" x2="0" y2="1">
        <stop offset="0" stop-color="#1e1e1e"/>
        <stop offset="0.5" stop-color="#3c3c3e"/>
        <stop offset="1" stop-color="#1e1e1e"/>
      </linearGradient>
      <linearGradient id="disc-fill" x1="0" y1="0" x2="0" y2="1">
        <stop offset="0" stop-color="#343436"/>
        <stop offset="0.45" stop-color="#5e5e60"/>
        <stop offset="0.75" stop-color="#545456"/>
        <stop offset="1" stop-color="#3a3a3c"/>
      </linearGradient>
      <polygon id="hex" points="0,-54 47,-27 47,27 0,54 -47,27 -47,-27"/>
    </defs>

    <!-- backdrop disc -->
    <circle class="disc-ring" cx="600" cy="614" r="570" fill="url(#ring-fill)"/>
    <circle class="disc" cx="600" cy="614" r="538" fill="url(#disc-fill)"/>

    <!-- contact band -->
    <circle class="contact-band" cx="600" cy="1390" r="414" fill="var(--red)"/>

    <!-- service hexagons with icons -->
    <g fill="var(--red)" stroke="none">
      <use href="#hex" x="226" y="342"/>
      <use href="#hex" x="278" y="434"/>
      <use href="#hex" x="331" y="526"/>
      <use href="#hex" x="278" y="618"/>
      <use href="#hex" x="226" y="710"/>
      <use href="#hex" x="278" y="802"/>
      <use href="#hex" x="226" y="894"/>
    </g>

    <g fill="none" stroke="var(--white)" stroke-width="2.4" stroke-linecap="round" stroke-linejoin="round">
      <!-- tick badge -->
      <g transform="translate(226 342)">
        <circle r="24" stroke-dasharray="6 3"/>
        <circle r="15"/>
        <path d="M-7 0 L-2 5 L8 -5"/>
      </g>
      <!-- car and wrench -->
      <g transform="translate(278 434)">
        <path d="M-26 10 V0 L-20 -10 H2 L8 0 V10 Z"/>
        <circle cx="-18" cy="3" r="2.5"/>
        <circle cx="0" cy="3" r="2.5"/>
        <path d="M-24 10 V15 M6 10 V15"/>
        <path d="M16 -20 V20 M11 -24 L16 -18 L21 -24 M11 24 L16 18 L21 24"/>
      </g>
      <!-- gear -->
      <g transform="translate(331 526)">
        <circle r="18"/>
        <circle r="8"/>
        <path d="M0 -27 V-18 M0 18 V27 M-27 0 H-18 M18 0 H27 M-19 -19 L-13 -13 M13 13 L19 19 M-19 19 L-13 13 M13 -13 L19 -19"/>
        <path d="M6 6 L22 22"/>
      </g>
      <!-- wheel -->
      <g transform="translate(278 618)">
        <circle r="26"/>
        <circle r="20"/>
        <circle r="5"/>
        <path d="M0 -20 V-5 M0 5 V20 M-20 0 H-5 M5 0 H20 M-14 -14 L-4 -4 M4 4 L14 14 M-14 14 L-4 4 M4 -4 L14 -14"/>
      </g>
      <!-- battery -->
      <g transform="translate(226 710)">
        <rect x="-26" y="-18" width="52" height="38" rx="2"/>
        <path d="M-18 -18 V-24 H-10 V-18 M10 -18 V-24 H18 V-18"/>
        <path d="M-26 -8 H26"/>
        <path d="M2 -2 L-4 7 H3 L-2 15"/>
      </g>
      <!-- parts -->
      <g transform="translate(278 802)">
        <circle cx="-12" cy="-20" r="5"/>
        <circle cx="12" cy="-20" r="5"/>
        <rect x="-18" y="-13" width="12" height="8"/>
        <rect x="6" y="-13" width="12" height="8"/>
        <path d="M-12 -5 V14 M12 -5 V14 M-17 0 H-7 M-17 5 H-7 M-17 10 H-7 M7 0 H17 M7 5 H17 M7 10 H17"/>
        <circle cx="-12" cy="20" r="5"/>
        <circle cx="12" cy="20" r="5"/>
      </g>
      <!-- car for sale -->
      <g transform="translate(226 894)">
        <rect x="-24" y="-28" width="48" height="14" rx="2"/>
        <path d="M-8 -14 V-9 M8 -14 V-9"/>
        <path d="M-26 16 V4 L-18 -8 H18 L26 4 V16 Z"/>
        <rect x="-8" y="6" width="16" height="5"/>
        <circle cx="-18" cy="8" r="3"/>
        <circle cx="18" cy="8" r="3"/>
        <path d="M-22 16 V22 M22 16 V22"/>
      </g>
    </g>
  </svg>

  <header class="brand">
    <h1 class="brand-name">HIGHGEAR</h1>
    <p class="brand-tagline">TOTAL AUTOMOTIVE</p>
  </header>

  <ul class="services">
    <li class="service" style="left:308px; top:342px;">WARRANT OF FITNESS</li>
    <li class="service" style="left:358px; top:434px;">VEHICLE SERVICING</li>
    <li class="service" style="left:408px; top:526px;">ALL MECHANICAL REPAIRS</li>
    <li class="service" style="left:358px; top:618px;">TYRES &amp; WHEEL ALIGNMENTS</li>
    <li class="service" style="left:306px; top:710px;">BATTERIES &amp; DIAGNOSTICS</li>
    <li class="service" style="left:358px; top:802px;">AUTOMOTIVE PARTS</li>
    <li class="service" style="left:308px; top:894px;">VEHICLE SALES</li>
  </ul>

  <footer class="contact">
    <p class="contact-address">48 Tamsin Road</p>
    <p class="contact-phone">07 542 3917</p>
  </footer>
</main>
</body>
</html>
```